Word Cloud Graphic Wallpaper design

The following sentences need to be put together in an ai file of the size : 70" wide and 108" high . This will be used as a wall paper. Inspirational image is attached. (We have also attached a rough idea showing you the wall it would go one- DO NOT REPLICATE THE LAYOUT OF THE SENTENCES-This only shows you how we will be using your file)

Sentences are:

Dentistry is not Expensive Neglect is!
Smiles are free but they are worth alot.
Don't Forget to Floss!
Put on your best SMILE everyday!
Be the reason someone smiles today.
Let your SMILE CHANGE THE WORLD, don't let the world change your smile.
Make your smile your signature accessory!

These should be in different fonts (clean modern fonts only please- no cursive or busy fonts - Helvetica Neue, Arial and fonts such as those are preferred) and sizes and should be easily legible (minimum font height 4"). Repetitions are ok if needed to fill space.

Font styles to use
Sans Serif

Requirements
Must have
• hese should be in different fonts (clean modern fonts only please- no cursive or busy fonts - Helvetica Neue, Arial and fonts such as those) and sizes and should be easily legible (minimum font height 4"). Repetitions are ok if needed to fill space.
Should not have
• Cursive, busy, fonts.

```html
<!DOCTYPE html>
<html lang="en">
<head>
<meta charset="utf-8">
<title>Smile Word Cloud Wallpaper</title>
<link rel="stylesheet" href="https://fonts.googleapis.com/css2?family=Montserrat:wght@700;800;900&family=Open+Sans:wght@300;400;600;700;800&display=swap">
<style>
  :root {
    --ink: #000000;
    --paper: #ffffff;
  }
  html, body {
    margin: 0;
    padding: 0;
    width: 802px;
    height: 1200px;
    overflow: hidden;
    background: var(--paper);
  }
  .wallpaper {
    position: relative;
    width: 802px;
    height: 1200px;
    overflow: hidden;
    background: var(--paper);
  }
  .board {
    position: absolute;
    left: 0;
    top: 0;
    width: 1000px;
    height: 1500px;
    transform: scale(0.802);
    transform-origin: 0 0;
    color: var(--ink);
  }
  .word {
    position: absolute;
    margin: 0;
    line-height: 1;
    white-space: nowrap;
  }
  .up {
    transform-origin: 0 0;
    transform: rotate(-90deg);
  }
  .sans { font-family: "Open Sans", sans-serif; }
  .geo  { font-family: "Montserrat", sans-serif; }
  .w300 { font-weight: 300; }
  .w400 { font-weight: 400; }
  .w600 { font-weight: 600; }
  .w700 { font-weight: 700; }
  .w800 { font-weight: 800; }
  .w900 { font-weight: 900; }
</style>
</head>
<body>
<main class="wallpaper">
  <div class="board">
    <!-- Dentistry is not expensive, neglect is! -->
    <p class="word sans w700 headline-dentistry" style="left:33px; top:2px; font-size:92px; letter-spacing:-3px;">DENTISTRY</p>
    <p class="word sans w400 up phrase-not-expensive" style="left:12px; top:530px; font-size:58px; letter-spacing:-2.5px;">IS NOT EXPENSIVE</p>
    <p class="word sans w800 up phrase-neglect" style="left:87px; top:530px; font-size:74px; letter-spacing:-1px;">NEGLECT IS!</p>

    <!-- Put on your best smile everyday! -->
    <p class="word sans w300 up phrase-put-on" style="left:168px; top:530px; font-size:129px; letter-spacing:-2px;">PUT ON</p>
    <p class="word sans w300 up phrase-your" style="left:296px; top:415px; font-size:124px; letter-spacing:-8px;">YOUR</p>
    <p class="word sans w400 up phrase-best" style="left:448px; top:212px; font-size:38px;">BEST</p>
    <p class="word sans w700 headline-smile-top" style="left:500px; top:55px; font-size:168px; letter-spacing:-5px;">SMILE</p>
    <p class="word sans w700 headline-everyday-top" style="left:436px; top:197px; font-size:103px; letter-spacing:-2px;">EVERYDAY!</p>

    <!-- Smiles are free but they are worth alot. -->
    <p class="word sans w400 phrase-free-1" style="left:440px; top:302px; font-size:46px;">Smiles are free but</p>
    <p class="word sans w400 phrase-free-2" style="left:440px; top:362px; font-size:46px;">they are worth alot.</p>

    <!-- Be the reason someone smiles today. -->
    <p class="word sans w800 phrase-reason" style="left:318px; top:418px; font-size:71px; letter-spacing:-1px;">BE THE REASON</p>
    <p class="word sans w700 phrase-someone" style="left:316px; top:492px; font-size:122px; letter-spacing:-2px;">someone</p>
    <p class="word sans w600 phrase-smiles-today" style="left:440px; top:628px; font-size:67px; letter-spacing:-1px;">smiles today.</p>

    <!-- Let your smile change the world -->
    <p class="word sans w400 phrase-let-your" style="left:18px; top:535px; font-size:76px;">Let your</p>
    <p class="word geo w900 headline-smile-left" style="left:18px; top:600px; font-size:126px; letter-spacing:-4px;">SMILE</p>
    <p class="word geo w900 phrase-change-world" style="left:18px; top:716px; font-size:72px; letter-spacing:-1px;">CHANGE THE WORLD,</p>
    <p class="word geo w700 phrase-dont-let" style="left:18px; top:808px; font-size:42px;">don't let the world change</p>
    <p class="word geo w700 phrase-your-smile" style="left:18px; top:866px; font-size:40px;">your smile.</p>

    <!-- Don't forget to floss! -->
    <p class="word sans w800 phrase-dont" style="left:278px; top:867px; font-size:74px; letter-spacing:-1px;">DON’T</p>
    <p class="word sans w800 phrase-forget" style="left:278px; top:937px; font-size:76px; letter-spacing:-1px;">FORGET</p>
    <p class="word sans w400 phrase-floss" style="left:274px; top:1022px; font-size:78px;">to floss !</p>

    <!-- Smiles are free but they are worth a lot. -->
    <p class="word geo w900 phrase-smiles" style="left:12px; top:926px; font-size:62px; letter-spacing:-1px;">SMILES</p>
    <p class="word geo w900 up phrase-are-free" style="left:4px; top:1490px; font-size:94px; letter-spacing:-1px;">ARE FREE</p>
    <p class="word geo w700 up phrase-worth-lot" style="left:106px; top:1490px; font-size:37px;">but they are worth a lot.</p>

    <!-- Put on your best smile everyday! (repeat) -->
    <p class="word sans w300 phrase-put" style="left:164px; top:994px; font-size:50px;">PUT</p>
    <p class="word sans w800 phrase-on" style="left:164px; top:1040px; font-size:52px;">ON</p>
    <p class="word sans w400 phrase-your-best" style="left:162px; top:1094px; font-size:90px;">your</p>
    <p class="word sans w800 phrase-best-bold" style="left:364px; top:1094px; font-size:80px;">BEST</p>
    <p class="word geo w900 headline-smile-lower" style="left:158px; top:1172px; font-size:126px; letter-spacing:-4px;">SMILE</p>
    <p class="word sans w300 phrase-everyday-lower" style="left:158px; top:1300px; font-size:82px; letter-spacing:-1px;">EVERYDAY!</p>

    <!-- Make your smile your signature accessory! -->
    <p class="word sans w400 up phrase-make-your" style="left:542px; top:1496px; font-size:130px; letter-spacing:-2px;">Make your</p>
    <p class="word sans w800 up headline-smile-vertical" style="left:662px; top:1496px; font-size:225px; letter-spacing:-6px;">SMILE</p>
    <p class="word sans w400 up phrase-signature" style="left:867px; top:1494px; font-size:102px; letter-spacing:-1px;">your signature accessory!</p>
  </div>
</main>
</body>
</html>
```